Business Card Design

Psychotherapy and Therapeutic Counselling

As well as Life Coaching.

Industry/Entity Type

Business

Contact Information for Business Card

Focus
Life Coaching Services
Confidential and Compassionate
KB FdSc Qualified Practitioner

Tel 07982514630

```html
<!DOCTYPE html>
<html lang="en">
<head>
<meta charset="utf-8">
<title>Haven – Business Card</title>
<link rel="stylesheet" href="https://fonts.googleapis.com/css2?family=Tenor+Sans&display=swap">
<style>
  :root {
    --paper: #ffffff;
    --ink: #111111;
    --wing-light: #f2f2f2;
    --wing-mid: #d6d6d6;
    --wing-dark: #bdbdbd;
  }
  html, body {
    margin: 0;
    padding: 0;
    width: 1200px;
    height: 791px;
    overflow: hidden;
    background: var(--paper);
  }
  .card {
    position: relative;
    width: 1200px;
    height: 791px;
    background: var(--paper);
    color: var(--ink);
    font-family: "Tenor Sans", "Optima", sans-serif;
    overflow: hidden;
  }
  .wing-art {
    position: absolute;
    left: 480px;
    top: 0;
    width: 720px;
    height: 791px;
    background:
      radial-gradient(ellipse 55% 75% at 35% 40%, var(--wing-mid) 0%, var(--wing-light) 55%, rgba(255,255,255,0) 80%),
      radial-gradient(ellipse 50% 30% at 75% 12%, var(--wing-dark) 0%, rgba(255,255,255,0) 75%);
    opacity: 0.8;
  }
  .contact {
    position: absolute;
    left: 35px;
    top: 92px;
    margin: 0;
    font-size: 35px;
    line-height: 46px;
  }
  .contact p { margin: 0; white-space: nowrap; }
  .contact__name {
    font-size: 44px;
    line-height: 48px;
    font-weight: 700;
  }
  .brand__name,
  .brand__services,
  .brand__promise {
    position: absolute;
    right: 36px;
    margin: 0;
    text-align: right;
    white-space: nowrap;
  }
  .brand__name {
    top: 505px;
    font-size: 170px;
    line-height: 170px;
    font-weight: 400;
    letter-spacing: 2px;
  }
  .brand__services {
    top: 659px;
    font-size: 38px;
    line-height: 44px;
    font-weight: 700;
  }
  .brand__promise {
    top: 705px;
    font-size: 36px;
    line-height: 44px;
  }
</style>
</head>
<body>
  <div class="card">
    <div class="wing-art" role="img" aria-label="Soft grey sweeping feather wing decoration"></div>

    <div class="contact">
      <p class="contact__name">KB</p>
      <p>FdSc Qualified</p>
      <p>NCTA Affiliated Practitioner</p>
      <p>t: 07982514630</p>
      <p>e: kb.practice@mailbox.co.uk</p>
    </div>

    <h1 class="brand__name">HAVEN</h1>
    <p class="brand__services">Therapeutic Counselling . Life Coaching</p>
    <p class="brand__promise">Confidential and Compassionate Service</p>
  </div>
</body>
</html>
```